Web Site Design for a Finance (lending) Company

We are opening a new subsidiary that focuses on lending money in the real estate industry. We need a web site designed to represent the business.

The business is lending money to real estate investors. A typical client/borrower will be looking to borrow money to buy a house, renovate it and then sell it at a profit, all within 12 months or less.

Company name is Brevand Finance. Our logo is attached.

Attached is a general outline for the web site. We're working on writing more text for each page but this should give you enough to get started with some ideas.

Competitor web site that I like a lot (as an example): https://quorvelfunding.com/. Many of the general items on this site match what we will need (description of loan programs, FAQ)

Target Market(s)

Real estate investors (generally individuals or small companies with just a few people) who are buying homes, renovating them and then selling them at a profit.

Industry/Entity Type

Finance

Coding

Coded - Design and coding required

Number of Pages Required

5+ page

Colors

Designer to choose colors to be used in the design.

Requirements
Must have
• Minimalist design. Clean lines without too much clutter. Some stock photography is ok but the photos should not be distracting. They should almost fade in to the background so that user can focus on the key information about what our company does instead. We are a finance company, not a design company, so the information about our products will be more interesting to site visitors than the art.
• Some minimalist examples from Snapboard:
• https://www.snapboard-example.com/explore/minimalist-web-design/
Nice to have
• If you search in seekly for "hard money lenders" you will find many examples of web sites from our competition. I have provided a link above to competitor web site that I like a lot.
• I have attached our logo in EPS format. Logo is green. Web site doesn't have to be green but it should be of a color that will work well with the logo.

```html
<!DOCTYPE html>
<html lang="en">
<head>
<meta charset="utf-8">
<title>Brevand Finance</title>
<link href="https://fonts.googleapis.com/css2?family=Urbanist:wght@500;600;700&family=Lato:wght@400;700&family=Arimo:wght@700&display=swap" rel="stylesheet">
<style>
:root{
  --green:#0b4a2d;
  --green-mid:#12603b;
  --grey-head:#8c8c8c;
  --text:#3a3a3a;
  --muted:#666;
  --line:#cfcfcf;
  --footer:#2f2f2f;
  --footer-line:#555;
  --white:#fff;
  --paper:#eeeeec;
}
*{box-sizing:border-box;margin:0;padding:0}
html,body{width:1200px;height:2311px;overflow:hidden}
body{font-family:"Lato",sans-serif;color:var(--text);background:var(--white);position:relative}
.heading{font-family:"Urbanist",sans-serif;font-weight:700;font-size:33px;text-align:center;color:var(--grey-head);letter-spacing:.2px}
.heading strong{color:var(--green);font-weight:700}
.divider{display:flex;align-items:center;justify-content:center;gap:10px;margin:16px auto 0;width:150px}
.divider span{flex:1;height:1px;background:var(--line)}
.divider i{width:9px;height:9px;border-radius:50%;background:#7a9d8b;display:block}
.btn{display:inline-block;background:var(--green);color:var(--white);font:700 13px "Lato",sans-serif;text-transform:uppercase;border-radius:20px;text-align:center}

/* top bar */
.topbar{height:37px;background:var(--green);display:flex;justify-content:flex-end;align-items:center;gap:26px;padding-right:120px;color:var(--white);font:700 14px "Lato",sans-serif}
.topbar .item{display:flex;align-items:center;gap:8px}
.topbar svg{width:22px;height:22px}

/* header */
.header{height:99px;display:flex;align-items:center;justify-content:space-between;padding:0 120px 0 122px}
.brand{display:flex;align-items:center;gap:12px;font:700 28px "Arimo",sans-serif;color:var(--green)}
.brand .mark{width:22px;height:22px;background:var(--green)}
.nav{display:flex;align-items:center;font:700 12px "Lato",sans-serif;text-transform:uppercase;color:#333}
.nav a{color:inherit;text-decoration:none;padding:0 24px;border-left:1px solid #ddd;line-height:16px}
.nav a:first-child{border-left:0;color:var(--green)}
.nav a:last-child{padding-right:0}

/* hero */
.hero{height:411px;position:relative;background:linear-gradient(100deg,#c79b6a 0%,#9a7a5e 25%,#5f5a55 55%,#2d3540 80%,#1d2631 100%)}
.hero-copy{position:absolute;left:0;right:0;top:172px;text-align:center;color:var(--white)}
.hero h1{font:700 31px "Urbanist",sans-serif;text-shadow:0 1px 4px rgba(0,0,0,.4)}
.hero p{font:400 19px "Lato",sans-serif;margin-top:12px;text-shadow:0 1px 3px rgba(0,0,0,.4)}
.hero .btn{margin-top:14px;width:163px;height:32px;line-height:32px}

/* welcome */
.welcome{height:285px;padding-top:40px;text-align:center}
.welcome p{width:960px;margin:22px auto 0;font-size:13.5px;line-height:24px;color:#444}
.welcome .btn{margin-top:17px;width:144px;height:33px;line-height:33px}

/* loans */
.loans{height:573px;position:relative;background:linear-gradient(180deg,#2b2e31 0%,#1f2326 50%,#2c302b 100%);padding-top:40px;text-align:center}
.loans .heading{color:var(--white)}
.loans .divider span{background:#777}
.loans .intro{width:900px;margin:20px auto 0;font-size:13.5px;line-height:20px;color:#e6e6e6}
.loan-cards{display:flex;gap:30px;width:960px;margin:20px auto 0}
.loan-card{width:465px;height:337px;background:var(--white);position:relative}
.loan-card .photo{height:278px}
.loan-card .caption{height:59px;display:flex;align-items:center;justify-content:space-between;padding-left:22px;font:700 22px "Urbanist",sans-serif;color:var(--green)}
.loan-card .arrow{width:72px;height:59px;background:#8d9496;clip-path:polygon(25% 0,100% 0,100% 100%,0 100%);display:flex;align-items:center;justify-content:center;padding-left:14px}

/* testimonials */
.testimonials{height:360px;background:var(--paper);padding-top:40px;position:relative}
.quotes{display:flex;gap:49px;width:958px;margin:34px 0 0 122px}
.quote{width:454px;position:relative}
.quote .bubble{height:126px;background:var(--white);border-radius:8px;padding:14px 16px;position:relative;box-shadow:0 1px 3px rgba(0,0,0,.08)}
.quote h3{font:700 16px "Urbanist",sans-serif;color:var(--green)}
.quote p{font-size:12px;line-height:17px;color:#555;width:330px;margin-top:4px}
.quote .mark{position:absolute;right:16px;top:4px;font:700 150px/1 "Urbanist",sans-serif;color:#e2e2e2}
.quote .avatar{position:absolute;left:23px;top:99px;width:80px;height:80px;border-radius:50%;border:3px solid var(--green);background:linear-gradient(180deg,#c9c3bd,#6c6f73)}
.quote .author{position:absolute;right:26px;top:141px;font:700 13px "Lato",sans-serif;color:#333}
.quote .author span{color:var(--green);letter-spacing:1px;margin-left:4px}
.chev{position:absolute;top:145px}

/* members */
.members{height:238px;padding-top:38px}
.badges{display:flex;gap:10px;width:960px;margin:34px auto 0}
.badge{width:128px;height:60px;border:1px solid #d8d8d8;border-radius:3px;display:flex;align-items:center;justify-content:center}
.badge i{display:block;width:70px;height:22px;background:#c9c9c9;border-radius:3px}

/* footer */
.footer{height:271px;background:var(--footer);color:#ddd;position:relative}
.col{position:absolute;top:32px}
.col h4{font:700 18px "Urbanist",sans-serif;color:var(--white);padding-bottom:12px;border-bottom:1px solid var(--footer-line)}
.col.contact{left:120px;width:405px}
.col.links{left:583px;width:175px}
.col.details{left:816px;width:264px}
.form{display:grid;grid-template-columns:195px 195px;grid-template-rows:30px 30px 30px;gap:14px;margin-top:16px;font-size:11.5px}
.field{height:30px;border:1px solid #888;padding:7px 10px;color:#eee}
.field.name{grid-column:1;grid-row:1}
.field.email{grid-column:1;grid-row:2}
.field.phone{grid-column:1;grid-row:3}
.field.tall{grid-column:2;grid-row:1/3;height:74px}
.submit{grid-column:2;grid-row:3;height:30px;background:#8b8f92;border-radius:15px;color:var(--white);font-weight:700;text-align:center;line-height:30px;font-size:12px}
.links ul{list-style:none;margin-top:12px}
.links li{font-size:12px;line-height:26px}
.links li::before{content:"›";margin-right:9px;color:#fff;font-weight:700}
.details .name{margin-top:14px;font:700 13px "Lato",sans-serif;color:var(--white)}
.details .blurb{font-size:11.5px;line-height:18px;margin-top:4px}
.details .row{display:flex;align-items:center;gap:12px;font-size:12px;margin-top:10px}
.details svg{width:13px;height:13px}

.bottombar{height:37px;background:var(--green);display:flex;align-items:center;justify-content:space-between;padding:0 120px;color:#eee;font-size:12.5px}
.bottombar strong{color:var(--white)}
.social{display:flex;gap:8px}
.social i{width:24px;height:24px;border:1.5px solid #fff;border-radius:50%;display:block}

.chat-tab{position:absolute;left:1163px;top:2060px;width:37px;height:115px;background:var(--white);border:1px solid #ccc;border-right:0;border-radius:6px 0 0 6px;overflow:hidden}
.chat-tab span{position:absolute;left:9px;top:8px;writing-mode:vertical-rl;transform:rotate(180deg);font:700 14px/18px "Lato",sans-serif;color:#222;white-space:nowrap}
.chat-tab b{position:absolute;left:0;bottom:0;width:37px;height:36px;background:var(--green-mid)}
</style>
</head>
<body>

<div class="topbar">
  <div class="item"><svg viewBox="0 0 24 24"><circle cx="12" cy="12" r="11" fill="none" stroke="#fff" stroke-width="1.5"/><path d="M8.5 7l2 2-1 1.5c.8 1.6 2 2.8 3.6 3.6l1.4-1 2 2-1.3 1.6C11.5 16.5 7.6 12.6 7 8.3z" fill="#fff"/></svg>(+014) 582-3907</div>
  <div class="item"><svg viewBox="0 0 24 24"><circle cx="12" cy="12" r="11" fill="none" stroke="#fff" stroke-width="1.5"/><rect x="6.5" y="8" width="11" height="8" fill="#fff"/><path d="M6.5 8l5.5 4.5L17.5 8" fill="none" stroke="#0b4a2d" stroke-width="1.2"/></svg>info@brevandfinance.com</div>
</div>

<header class="header">
  <div class="brand"><span class="mark"></span>Brevand Finance</div>
  <nav class="nav">
    <a>Home</a><a>About Us</a><a>Types Of Loans ˅</a><a>Resources</a><a>Contact Us ˅</a>
  </nav>
</header>

<section class="hero" role="img" aria-label="Photo of a model house beside a handshake over a signed contract">
  <div class="hero-copy">
    <h1>Local Real Estate Experts Lending To Local Real Estate Investors</h1>
    <p>Fix And Flip Loans &nbsp;|&nbsp; Commercial Hard Money Loans</p>
    <span class="btn">Contact Us Today</span>
  </div>
</section>

<section class="welcome">
  <h2 class="heading">Welcome To <strong>Brevand Finance</strong></h2>
  <div class="divider"><span></span><i></i><span></span></div>
  <p>Brevand Finance is a local business with local knowledge and strong industry relationships. A partner with a wide network who offers value added services. Brevand has an established pool of experienced investors available for your real estate investment needsIt has survived not only five centuries, but also the leap into electronic typesetting, remaining essentially unchanged. It was popularised in the 1960s with the release.</p>
  <span class="btn">Learn More</span>
</section>

<section class="loans" role="img" aria-label="Dimmed photo of a house at dusk behind the loan cards">
  <h2 class="heading">Types Of Loans</h2>
  <div class="divider"><span></span><i></i><span></span></div>
  <p class="intro">Lorem ipsum dolor sit amet, consectetur adipiscing elit, sed do eiusmod tempor incididunt ut labore et dolore magna aliqua. Ut enim ad minim veniam, quis nostrud exercitation ullamco laboris nisi ut aliquip ex ea commodo consequat.</p>
  <div class="loan-cards">
    <article class="loan-card">
      <div class="photo" role="img" aria-label="Hands holding a small model house over banknotes" style="background:linear-gradient(135deg,#e8e2da 0%,#c87a4a 45%,#9fa58c 100%)"></div>
      <div class="caption">Fix And Flip Loans<span class="arrow"><svg width="18" height="14" viewBox="0 0 18 14"><path d="M2 2l5 5-5 5M9 2l5 5-5 5" fill="none" stroke="#fff" stroke-width="2"/></svg></span></div>
    </article>
    <article class="loan-card">
      <div class="photo" role="img" aria-label="Model house with a red roof on a calculator and paperwork" style="background:linear-gradient(135deg,#7f8a86 0%,#d8dcd6 45%,#c7544a 70%,#e9ece8 100%)"></div>
      <div class="caption">Commercial Hard Money Loans<span class="arrow"><svg width="18" height="14" viewBox="0 0 18 14"><path d="M2 2l5 5-5 5M9 2l5 5-5 5" fill="none" stroke="#fff" stroke-width="2"/></svg></span></div>
    </article>
  </div>
</section>

<section class="testimonials">
  <h2 class="heading">Client <strong>Testimonials</strong></h2>
  <div class="divider"><span></span><i></i><span></span></div>
  <svg class="chev" style="left:74px" width="16" height="32" viewBox="0 0 16 32"><path d="M13 2L3 16l10 14" fill="none" stroke="#bbb" stroke-width="1.5"/></svg>
  <svg class="chev" style="left:1110px" width="16" height="32" viewBox="0 0 16 32"><path d="M3 2l10 14L3 30" fill="none" stroke="#bbb" stroke-width="1.5"/></svg>
  <div class="quotes">
    <div class="quote">
      <div class="bubble"><span class="mark">”</span><h3>Lorem ipsum dolor sit amet, consecet uera.</h3><p>Lorem ipsum dolor sit amet, consectet uer adipiscing elit, sed diam nonummy nibh euis mod tincidun nt ut laoreetml dolore magna aliquam erat volutpat.</p></div>
      <div class="avatar" role="img" aria-label="Client portrait"></div>
      <div class="author">- Miss Marla Quintero<span>★★★★★</span></div>
    </div>
    <div class="quote">
      <div class="bubble"><span class="mark">”</span><h3>Lorem ipsum dolor sit amet, consecet uera.</h3><p>Lorem ipsum dolor sit amet, consectet uer adipiscing elit, sed diam nonummy nibh euis mod tincidun nt ut laoreetml dolore magna aliquam erat volutpat.</p></div>
      <div class="avatar" role="img" aria-label="Client portrait"></div>
      <div class="author">- Miss Marla Quintero<span>★★★★★</span></div>
    </div>
  </div>
</section>

<section class="members">
  <h2 class="heading">Our <strong>Industry Member</strong></h2>
  <div class="divider"><span></span><i></i><span></span></div>
  <div class="badges">
    <div class="badge"><i></i></div><div class="badge"><i></i></div><div class="badge"><i></i></div><div class="badge"><i></i></div><div class="badge"><i></i></div><div class="badge"><i></i></div><div class="badge"><i></i></div>
  </div>
</section>

<footer class="footer">
  <div class="col contact">
    <h4>Contact Us</h4>
    <div class="form">
      <div class="field name">Name</div>
      <div class="field email">Email Address</div>
      <div class="field phone">Phone Number</div>
      <div class="field tall">How you heard about us</div>
      <div class="submit">SUBMIT</div>
    </div>
  </div>
  <div class="col links">
    <h4>Quick Links</h4>
    <ul><li>Home</li><li>About Us</li><li>Types Of Loans</li><li>Resources</li><li>Contact Us</li></ul>
  </div>
  <div class="col details">
    <h4>Contact Details</h4>
    <div class="name">BREVAND FINANCE</div>
    <p class="blurb">Lorem Ipsum is simply dummy text of there is printing and typesetting industry.</p>
    <div class="row"><svg viewBox="0 0 24 24"><path d="M5 3l5 5-2 3c1.5 3 3.5 5 6 6l3-2 5 5-3 3C10 22 2 14 2 6z" fill="#fff"/></svg>(+014) 582-3907</div>
    <div class="row"><svg viewBox="0 0 24 24"><rect x="6" y="2" width="12" height="6" fill="#fff"/><rect x="2" y="9" width="20" height="9" rx="2" fill="#fff"/><rect x="6" y="15" width="12" height="7" fill="#fff" stroke="#2f2f2f"/></svg>(+014) 582-3907</div>
    <div class="row"><svg viewBox="0 0 24 24"><rect x="2" y="5" width="20" height="14" fill="#fff"/><path d="M2 5l10 8 10-8" fill="none" stroke="#2f2f2f" stroke-width="1.5"/></svg>info@brevandfinance.com</div>
  </div>
</footer>

<div class="bottombar">
  <div>Copyright © 2017 <strong>Brevand Finance</strong> | All Right Reserved.</div>
  <div class="social"><i></i><i></i><i></i><i></i></div>
</div>

<div class="chat-tab"><span>Live Chat</span><b></b></div>

</body>
</html>
```